Business Cards for our company

Hi there,

we have successfully designed a logo with ArtFlock and would like now to design our business cards. We would like to keep the colours and the look-and-feel of the logo. Please send in variations with two or three colours and one or two sides. I promise to respond to every single submission.

Many thanks and happy new year.

All the best,
Wilfried

Target Market(s)

B2B

Industry/Entity Type

Trade

Contact Information for Business Card

We have successfully designed a logo with ArtFlock and would like now to design our business cards. We would like to keep the colours and the look-and-feel of the logo. Please send in variations with two or three colours and one or two sides. I promise to respond to every single submission.

Font styles to use
Serif
Sans Serif
Script

Requirements
Must have
• These information should be on the business card, grouped as you suggest, and we think using small pictograms for mobile, email, etc is pretty helpful:
• Wilfried Tammler (first and second name)
• Geschäftsführer/ Managing Director (title)
• KoR Warenkontor GmbH (company name and legal form)
• Ostheimer Str. 18/3 (street and house number)
• 72816 Lindenfeld (zip code and town)
• +491709384562 (mobile)
• +4971569027341 (work)
• w.tammler@kor-warenkontor.example (email)
• www.kor-warenkontor.example (web)
Nice to have
• Spectacular and interesting layout and design. You look at it and think, wow, that's not the normal stuff.
• We think of ourselves as bridge-builders between businesses (international producers on the one hand, and retail chains on the other hand) and we translate, organise and manage projects where both partners are involved, but it's difficult for them to cooperate due to language barriers and different working cultures.
• This is why we have the n between the B's shaped as a bridge, and the green arc supports this idea. Maybe you could play with this idea...
Should not have
• the standard layout that everybody has

```html
<!DOCTYPE html>
<html lang="de">
<head>
<meta charset="utf-8">
<title>KoR Warenkontor – Business Card</title>
<link rel="stylesheet" href="https://fonts.googleapis.com/css2?family=Source+Sans+3:wght@400;600;700&display=swap">
<style>
  :root {
    --backdrop-top: #2a2a2a;
    --backdrop-bottom: #050505;
    --card-grey: #c5c7ca;
    --brand-green: #2fad4a;
    --green-light: #7fd293;
    --ink: #111111;
    --white: #ffffff;
    --silver-edge: #b9bab9;
    --silver-center: #ffffff;
  }
  * { margin: 0; padding: 0; box-sizing: border-box; }
  html, body { width: 1200px; height: 900px; overflow: hidden; }
  body {
    position: relative;
    background: linear-gradient(180deg, var(--backdrop-top) 0%, #161616 55%, var(--backdrop-bottom) 100%);
    font-family: "Source Sans 3", "Myriad Pro", Arial, sans-serif;
  }
  .card {
    position: absolute;
    top: 300px;
    width: 442px;
    height: 272px;
    border-radius: 10px;
    overflow: hidden;
  }
  .card--front { left: 152px; background: var(--card-grey); }
  .card--back {
    left: 622px;
    background: radial-gradient(ellipse 60% 75% at 50% 45%, var(--silver-center) 0%, #e9eaea 40%, var(--silver-edge) 100%);
  }
  .front-shape { position: absolute; inset: 0; }
  .wordmark {
    position: absolute;
    left: 20px;
    top: 100px;
    width: 150px;
    text-align: center;
    font-weight: 700;
    font-size: 62px;
    line-height: 1;
    color: var(--ink);
    letter-spacing: 1px;
  }
  .contact {
    position: absolute;
    right: 23px;
    top: 33px;
    text-align: right;
    color: var(--white);
  }
  .contact__name { font-weight: 700; font-size: 18px; line-height: 22px; }
  .contact__title { font-size: 14.5px; line-height: 19px; }
  .contact__address { margin-top: 44px; font-size: 14.5px; line-height: 19.5px; }
  .contact__lines { margin-top: 17px; list-style: none; font-size: 14.5px; line-height: 18.3px; }
  .contact__lines li { display: flex; justify-content: flex-end; align-items: center; gap: 6px; }
  .contact__lines svg { width: 10px; height: 10px; fill: var(--white); flex: none; }
  .back-name {
    position: absolute;
    left: 0; right: 0;
    top: 108px;
    text-align: center;
    font-weight: 700;
    font-size: 40px;
    line-height: 1;
    color: var(--ink);
  }
  .back-name__dot {
    display: inline-block;
    width: 12px; height: 12px;
    border-radius: 50%;
    background: var(--brand-green);
    margin-left: 10px;
    vertical-align: middle;
  }
</style>
</head>
<body>
  <section class="card card--front">
    <svg class="front-shape" viewBox="0 0 442 272" aria-hidden="true">
      <rect x="151" y="0" width="291" height="272" fill="var(--brand-green)"/>
      <path d="M151 0 C 247 50 247 222 151 272 Z" fill="var(--green-light)" opacity="0.7"/>
      <path d="M0 0 H151 C 200 60 200 212 151 272 H0 Z" fill="var(--card-grey)"/>
    </svg>
    <div class="wordmark">KoR</div>
    <div class="contact">
      <p class="contact__name">Wilfried Tammler</p>
      <p class="contact__title">Managing Director</p>
      <p class="contact__address">Ostheimer Str. 18/3<br>72816 Lindenfeld</p>
      <ul class="contact__lines">
        <li>+491709384562
          <svg viewBox="0 0 10 10"><path d="M1 3 Q5 0 9 3 L8 4.5 L6.5 4 L6.5 3 Q5 2.5 3.5 3 L3.5 4 L2 4.5 Z M2.5 5 H7.5 L8.5 8 H1.5 Z"/></svg>
        </li>
        <li>+4971569027341
          <svg viewBox="0 0 10 10"><path d="M3 0.5 H7 Q8 0.5 8 1.5 V8.5 Q8 9.5 7 9.5 H3 Q2 9.5 2 8.5 V1.5 Q2 0.5 3 0.5 Z M3 2 V7.5 H7 V2 Z"/></svg>
        </li>
        <li>tammler@kor-warenkontor.example
          <svg viewBox="0 0 10 10"><path d="M1 2.5 H9 V7.5 H1 Z M1.5 3 L5 5.5 L8.5 3"/></svg>
        </li>
        <li>www.kor-warenkontor.example
          <svg viewBox="0 0 10 10"><circle cx="5" cy="5" r="4.5"/></svg>
        </li>
      </ul>
    </div>
  </section>

  <section class="card card--back">
    <p class="back-name">KoR Warenkontor<span class="back-name__dot"></span></p>
  </section>
</body>
</html>
```